Year 12 Chemistry Workbook illustrations and diagrams

We are producing a Chemistry Workbook for senior high-school students in South Australia and require a designer to create illustrations including detailed diagrams and graphs for our upcoming publication.

The attached files are illustrations that we'd like to have recreated, with your own personal style incorporated.

We will require you to do the following:
- Create vector artwork
- Supply AI files
- Use the font helvetica neue 45 light, or its italic variation
- Use full colour wherever possible
- Please use 100% black, not RGB black/eye-dropped black

Target Market(s)

Senior high school students

Industry/Entity Type

School

Font styles to use
Sans Serif

Colors

Designer to choose colors to be used in the design.

Requirements
Must have
• - Create vector artwork
• - Supply AI files
• - Use the font helvetica neue 45 light, or its italic variation
• - Use full colour wherever possible
• - Please use 100% black, not RGB black/eye-dropped black
Should not have
• Please do not use RGB black/eye-dropped black

```html
<!DOCTYPE html>
<html lang="en">
<head>
<meta charset="UTF-8">
<title>Stages in the production of bioethanol</title>
<link rel="stylesheet" href="https://fonts.googleapis.com/css2?family=Inter:ital,wght@0,300;0,400;1,300&display=swap">
<style>
  :root {
    --ink: #000000;
    --paper: #fbfbfb;
    --panel-top: #a6cfee;
    --panel-bottom: #5ca4dd;
    --panel-edge: #1576cf;
    --arrow-red: #e3141c;
    --feed-navy: #293f74;
    --milling: #e5262b;
    --pretreat: #ef7b2a;
    --filtration: #f7c21c;
    --fermentation: #19893d;
    --distillation: #1e8fe2;
    --liquefaction: #6d4994;
    --hydrolysis: #ef6e6a;
    --box-text: #ffffff;
  }
  html, body {
    margin: 0;
    padding: 0;
    width: 1200px;
    height: 864px;
    overflow: hidden;
    background: var(--paper);
  }
  .figure {
    position: relative;
    width: 1200px;
    height: 864px;
    font-family: "Inter", sans-serif;
    font-weight: 300;
    color: var(--ink);
  }
  .intro {
    position: absolute;
    top: 38px;
    left: 0;
    width: 1200px;
    margin: 0;
    text-align: center;
    font-size: 29px;
    line-height: 36px;
  }
  .flow {
    position: absolute;
    top: 0;
    left: 0;
  }
  .caption {
    position: absolute;
    top: 715px;
    left: 0;
    width: 1200px;
    margin: 0;
    text-align: center;
    font-size: 40px;
  }
  .instruction {
    position: absolute;
    top: 782px;
    left: 0;
    width: 1200px;
    margin: 0;
    text-align: center;
    font-size: 22px;
    font-style: italic;
  }
  .step-label { fill: var(--box-text); font-size: 19px; font-weight: 400; text-anchor: middle; dominant-baseline: central; }
  .side-label { fill: var(--ink); font-size: 19px; font-weight: 300; }
  .product { fill: var(--ink); font-size: 27px; font-weight: 300; }
  .route-tag { fill: var(--ink); font-size: 26px; font-weight: 300; }
  .step { stroke: rgba(255,255,255,0.75); stroke-width: 2; }
  .flow-arrow { stroke: var(--arrow-red); stroke-width: 3.5; fill: none; }
  .feed-arrow { stroke: var(--feed-navy); stroke-width: 10; fill: none; }
</style>
</head>
<body>
<div class="figure">
  <p class="intro">The ethanol content is limited by the types of yeast and enzymes present<br>during fermentation. Higher concentrations of ethanol are obtained<br>through fractional distillation (Figure 4.1.2).</p>

  <svg class="flow" width="1200" height="864" viewBox="0 0 1200 864" xmlns="http://www.w3.org/2000/svg">
    <defs>
      <linearGradient id="panelFill" x1="0" y1="0" x2="0" y2="1">
        <stop offset="0" stop-color="var(--panel-top)"/>
        <stop offset="1" stop-color="var(--panel-bottom)"/>
      </linearGradient>
      <marker id="redHead" viewBox="0 0 10 10" refX="9" refY="5" markerWidth="3.2" markerHeight="3.2" orient="auto">
        <path d="M0 0 L10 5 L0 10 z" fill="var(--arrow-red)"/>
      </marker>
    </defs>

    <rect x="71" y="166" width="1058" height="530" rx="32" fill="url(#panelFill)" stroke="var(--panel-edge)" stroke-width="5"/>

    <!-- Route a: sugarcane -->
    <g class="route-a">
      <path class="feed-arrow" d="M193 241 H160 V262"/>
      <path d="M150 261 H170 L160 273 z" fill="var(--feed-navy)"/>
      <text class="side-label" x="202" y="248">Sugarcane</text>

      <rect class="step" x="110" y="272" width="98" height="42" rx="7" fill="var(--milling)"/>
      <text class="step-label" x="159" y="293">Milling</text>
      <rect class="step" x="230" y="272" width="164" height="42" rx="7" fill="var(--pretreat)"/>
      <text class="step-label" x="312" y="292">Pretreatment</text>
      <rect class="step" x="422" y="272" width="122" height="42" rx="7" fill="var(--filtration)"/>
      <text class="step-label" x="483" y="293">Filtration</text>
      <rect class="step" x="566" y="272" width="175" height="42" rx="7" fill="var(--fermentation)"/>
      <text class="step-label" x="653" y="293">Fermentation</text>
      <rect class="step" x="759" y="272" width="151" height="42" rx="7" fill="var(--distillation)"/>
      <text class="step-label" x="835" y="293">Distillation</text>

      <line class="flow-arrow" x1="208" y1="293" x2="229" y2="293" marker-end="url(#redHead)"/>
      <line class="flow-arrow" x1="394" y1="293" x2="421" y2="293" marker-end="url(#redHead)"/>
      <line class="flow-arrow" x1="544" y1="293" x2="565" y2="293" marker-end="url(#redHead)"/>
      <line class="flow-arrow" x1="741" y1="293" x2="758" y2="293" marker-end="url(#redHead)"/>
      <line class="flow-arrow" x1="910" y1="293" x2="992" y2="293" marker-end="url(#redHead)"/>

      <text class="side-label" x="892" y="259">Dehydration</text>
      <text class="product" x="1006" y="300">Ethanol</text>

      <line class="flow-arrow" x1="160" y1="314" x2="160" y2="350" marker-end="url(#redHead)"/>
      <text class="side-label" x="186" y="348">Bagasse</text>
      <text class="side-label" x="160" y="379" text-anchor="middle">Boiler</text>

      <line class="flow-arrow" x1="483" y1="314" x2="483" y2="350" marker-end="url(#redHead)"/>
      <text class="side-label" x="483" y="376" text-anchor="middle">Cake</text>

      <line class="flow-arrow" x1="654" y1="350" x2="654" y2="315" marker-end="url(#redHead)"/>
      <text class="side-label" x="654" y="376" text-anchor="middle">Yeast</text>

      <text class="route-tag" x="1039" y="377">a)</text>
    </g>

    <!-- Route b: dry ground corn -->
    <g class="route-b">
      <path class="feed-arrow" d="M188 416 H155 V436"/>
      <path d="M145 435 H165 L155 447 z" fill="var(--feed-navy)"/>
      <text class="side-label" x="198" y="423">Dry ground corn</text>

      <rect class="step" x="106" y="446" width="98" height="42" rx="7" fill="var(--milling)"/>
      <text class="step-label" x="155" y="466">Milling</text>
      <rect class="step" x="226" y="446" width="164" height="42" rx="7" fill="var(--liquefaction)"/>
      <text class="step-label" x="308" y="467">Liquefaction</text>
      <rect class="step" x="415" y="446" width="321" height="42" rx="7" fill="var(--hydrolysis)"/>
      <text class="step-label" x="575" y="466">Hydrolisis &amp; Fermentation</text>
      <rect class="step" x="755" y="446" width="151" height="42" rx="7" fill="var(--distillation)"/>
      <text class="step-label" x="830" y="467">Distillation</text>

      <line class="flow-arrow" x1="204" y1="467" x2="225" y2="467" marker-end="url(#redHead)"/>
      <line class="flow-arrow" x1="390" y1="467" x2="414" y2="467" marker-end="url(#redHead)"/>
      <line class="flow-arrow" x1="736" y1="467" x2="754" y2="467" marker-end="url(#redHead)"/>
      <line class="flow-arrow" x1="906" y1="467" x2="992" y2="467" marker-end="url(#redHead)"/>

      <text class="side-label" x="889" y="432">Dehydration</text>
      <text class="product" x="1006" y="477">Ethanol</text>

      <line class="flow-arrow" x1="306" y1="524" x2="306" y2="489" marker-end="url(#redHead)"/>
      <text class="side-label" x="306" y="550" text-anchor="middle">Enzyme</text>
      <line class="flow-arrow" x1="501" y1="524" x2="501" y2="489" marker-end="url(#redHead)"/>
      <text class="side-label" x="501" y="550" text-anchor="middle">Enzyme</text>
      <line class="flow-arrow" x1="651" y1="524" x2="651" y2="489" marker-end="url(#redHead)"/>
      <text class="side-label" x="651" y="552" text-anchor="middle">Yeast</text>

      <line class="flow-arrow" x1="830" y1="489" x2="830" y2="524" marker-end="url(#redHead)"/>
      <text class="side-label" x="830" y="552" text-anchor="middle">Solids</text>
      <line class="flow-arrow" x1="830" y1="564" x2="830" y2="598" marker-end="url(#redHead)"/>
      <text class="side-label" x="856" y="584">Drying</text>
      <text class="side-label" x="830" y="626" text-anchor="middle">Distillers Dry Grains</text>

      <text class="route-tag" x="1039" y="555">b)</text>
    </g>
  </svg>

  <p class="caption">Figure 4.1.2: Stages in the production of biotethanol.</p>
  <p class="instruction">(Construct flow diagrams.)</p>
</div>
</body>
</html>
```